Electronic Time-sheet for phones

I need a time-sheet that can be accessed on the phone, be completed, then have the ability to electronically sign. The time sheet needs to be used two fold for supervision to verify hours and quantities and also for the client to be able to electronically sign. The time-sheet should be daily or weekly if we can get the data to fit. We are trying to streamline field supervisors having to log on to a computer to access a server just to do time-sheets. We need it to be user friendly. We need to have two places to have electronic signatures. One for supervisor or authorized representative and the other for the client to sign.

Target Market(s)

Industrial clients

Industry/Entity Type

Oil And Gas

Requirements
Must have
• hours, quantities, project name, location, signature line etc
Nice to have
• n/a
Should not have
• n/a

```html
<!DOCTYPE html>
<html lang="en">
<head>
<meta charset="utf-8">
<title>Supervisor: Viewing time-sheet</title>
<link rel="stylesheet" href="https://fonts.googleapis.com/css2?family=Mulish:wght@300;400&family=Roboto:wght@400;500;700&display=swap">
<style>
  :root {
    --page-bg: #ffffff;
    --navy: #13294b;
    --text: #555555;
    --text-dark: #333333;
    --ios-blue: #1a7bf0;
    --line: #d4d4d4;
    --icon-grey: #a8a8a8;
    --tab-bg: #fafafa;
  }
  * { box-sizing: border-box; margin: 0; padding: 0; }
  html, body { width: 1200px; height: 1000px; overflow: hidden; background: var(--page-bg); }
  body { position: relative; font-family: "Roboto", Arial, sans-serif; color: var(--text); }

  /* Annotation */
  .step-badge {
    position: absolute; left: 254px; top: 113px; width: 46px; height: 46px;
    border-radius: 50%; background: var(--navy); color: #fff;
    font-size: 14px; display: flex; align-items: center; justify-content: center;
  }
  .notes-title {
    position: absolute; left: 161px; top: 183px;
    font-family: "Mulish", Arial, sans-serif; font-weight: 300;
    font-size: 29px; line-height: 37px; color: #111; letter-spacing: 0.3px;
  }
  .notes-eye { position: absolute; left: 161px; top: 282px; }
  .notes-body {
    position: absolute; left: 191px; top: 280px; width: 345px;
    font-size: 13.4px; line-height: 16px; color: var(--text);
  }
  .notes-body h3 { font-size: 13.4px; font-weight: 700; margin-bottom: 0; }
  .notes-body p { margin-bottom: 16px; }
  .notes-body .sign-off { margin-top: 40px; }

  /* Screen */
  .screen {
    position: absolute; left: 569px; top: 142px; width: 410px; height: 693px;
    background: #fff; border: 1px solid #e2e2e2; overflow: hidden;
  }
  .status-bar {
    position: absolute; left: 0; top: 0; width: 100%; height: 20px;
    font-size: 12px; color: #111; display: flex; align-items: center;
    justify-content: space-between; padding: 0 6px;
  }
  .status-center { position: absolute; left: 0; right: 0; text-align: center; }
  .go-back {
    position: absolute; left: 17px; top: 43px; font-size: 18px; color: var(--ios-blue);
    display: flex; align-items: center; gap: 4px;
  }
  .brand {
    position: absolute; right: 16px; top: 40px;
    font-weight: 700; font-size: 28px; color: var(--navy); letter-spacing: 1px;
  }

  .sheet {
    position: absolute; left: 17px; top: 98px; width: 376px; height: 527px;
    border: 1px solid var(--line); border-radius: 5px; padding: 0 13px;
  }
  .sheet-head {
    display: flex; justify-content: space-between; align-items: center;
    height: 61px; border-bottom: 1px solid var(--line); font-size: 14.5px;
  }
  .person, .sheet-date { display: flex; align-items: center; gap: 9px; }
  .fields { list-style: none; font-size: 14.5px; color: var(--text); }
  .fields li { position: absolute; left: 13px; }

  .tab-bar {
    position: absolute; left: 0; bottom: 0; width: 100%; height: 53px;
    border-top: 1px solid #e4e4e4; background: var(--tab-bg);
    display: flex; justify-content: space-around; padding: 0 10px;
  }
  .tab { display: flex; flex-direction: column; align-items: center; width: 110px; padding-top: 6px;
    font-size: 8px; color: #666; gap: 3px; }
  .tab.active { color: var(--ios-blue); }
</style>
</head>
<body>

<section class="notes">
  <div class="step-badge">4.2</div>
  <h1 class="notes-title">Supervisor:<br>Viewing time-sheet</h1>
  <svg class="notes-eye" width="18" height="12" viewBox="0 0 18 12" aria-hidden="true">
    <path d="M1 6 Q9 -2 17 6 Q9 14 1 6 Z" fill="var(--ios-blue)"/>
    <circle cx="9" cy="6" r="3" fill="#fff"/><circle cx="9" cy="6" r="1.6" fill="var(--ios-blue)"/>
  </svg>
  <div class="notes-body">
    <h3>View Time-sheet</h3>
    <p>This shows the same data in a read-only<br>view that the supervisor has entered shown<br>in screen 5.</p>
    <p>At the end of this view is the signed status<br>for this time sheet. If it has been signed by<br>supervisor, you can display their name here.<br>If client has signed it, you can show their name<br>here. If no one has signed it, it can be empty.</p>
    <p>On exporting a time-sheet (by clicking the<br>export icon shown in screen 4.1), this same view<br>will be converted to a pdf.</p>
    <p class="sign-off">I hope I have cleared your question.<br>If you need further elaboration in design or have<br>an idea, please let me know. Thanks!</p>
  </div>
</section>

<main class="screen">
  <div class="status-bar">
    <span>●●●○○ GS</span>
    <span class="status-center">9:41 AM</span>
    <span>58 % ▭</span>
  </div>

  <div class="go-back">
    <svg width="10" height="16" viewBox="0 0 10 16" aria-hidden="true"><path d="M8 2 L2 8 L8 14" fill="none" stroke="var(--ios-blue)" stroke-width="2"/></svg>
    Go Back
  </div>
  <div class="brand">KESTREL</div>

  <article class="sheet">
    <header class="sheet-head">
      <div class="person">
        <svg width="32" height="32" viewBox="0 0 32 32" aria-hidden="true">
          <circle cx="16" cy="16" r="15" fill="none" stroke="#555" stroke-width="1.5"/>
          <circle cx="16" cy="12" r="5.5" fill="#666"/>
          <path d="M6 27 Q16 15 26 27 Z" fill="#666"/>
        </svg>
        Alex Rowan
      </div>
      <div class="sheet-date">
        <svg width="18" height="26" viewBox="0 0 18 26" aria-hidden="true"><path d="M6 1 H17 V25 H1 V6 Z" fill="none" stroke="var(--icon-grey)" stroke-width="2"/></svg>
        5 November, 2018
      </div>
    </header>
    <ul class="fields">
      <li style="top:75px">Employee No: 450</li>
      <li style="top:104px">Project Name: ABC Project</li>
      <li style="top:133px">Project No:112</li>
      <li style="top:162px">Phase Code:8721A</li>
      <li style="top:191px">Project No:112</li>
      <li style="top:223px">Location: Xyz</li>
      <li style="top:255px">Hours: 10</li>
      <li style="top:287px">Quantity: 2</li>
      <li style="top:319px">Parameter A</li>
      <li style="top:351px">Parameter B</li>
      <li style="top:383px">Parameter C</li>
      <li style="top:415px">Parameter D</li>
      <li style="top:447px">Comments: Nil</li>
      <li style="top:476px;left:14px">Signed by Supervisor: [Supervisor Name[</li>
      <li style="top:507px;left:14px">Signed by Client: [Client Name]</li>
    </ul>
  </article>

  <nav class="tab-bar">
    <div class="tab active">
      <svg width="20" height="26" viewBox="0 0 20 26" aria-hidden="true"><path d="M7 1 H19 V25 H1 V7 Z" fill="none" stroke="var(--ios-blue)" stroke-width="2"/></svg>
      Current Week
    </div>
    <div class="tab">
      <svg width="30" height="26" viewBox="0 0 30 26" aria-hidden="true">
        <path d="M5 13 A10 10 0 1 1 8 20" fill="none" stroke="var(--icon-grey)" stroke-width="2"/>
        <path d="M1 10 L5 14 L9 10" fill="none" stroke="var(--icon-grey)" stroke-width="2"/>
        <rect x="12" y="9" width="8" height="10" fill="var(--icon-grey)"/>
      </svg>
      History
    </div>
    <div class="tab">
      <svg width="28" height="26" viewBox="0 0 28 26" aria-hidden="true">
        <path d="M8 6 A10 10 0 1 0 20 6" fill="none" stroke="var(--icon-grey)" stroke-width="2.5"/>
        <line x1="14" y1="1" x2="14" y2="12" stroke="var(--icon-grey)" stroke-width="2.5"/>
      </svg>
      Logout
    </div>
  </nav>
</main>

</body>
</html>
```